Order Management User Interface

I need a new design for our order management screens. They need to be end user friendly and contain the data in an easy to read format. These are online orders. I have attached 3 images from the development solution. For now I just need a new UI and ideally would like it delivered in html so we can easily adapt. The screen has multiple tabs to display the different types of data we store. Ideally the end user needs to see customer focused information first.
I have uploaded an example of a different order view that i like.
Industry/Entity Type
Fashion Retail
Coding
Coded - Design and coding required
Number of Pages Required
1 page

```html
<!DOCTYPE html>
<html lang="en">
<head>
<meta charset="utf-8">
<title>Order Management – Addresses</title>
<link href="https://fonts.googleapis.com/css2?family=Poppins:wght@400;500;600;700&display=swap" rel="stylesheet">
<style>
:root{
  --sidebar:#1f2431;
  --bg:#f3f3f3;
  --panel:#ffffff;
  --field:#f3f3f3;
  --green:#2fd38a;
  --dark:#1f2431;
  --text:#222631;
  --muted:#5d606a;
  --line:#e4e4e4;
  --line-strong:#d6d6d6;
  --red:#ef5350;
}
*{box-sizing:border-box;margin:0;padding:0}
html,body{width:1200px;height:1022px;overflow:hidden}
body{font-family:'Poppins',sans-serif;background:var(--bg);color:var(--text);position:relative}
.sidebar{position:absolute;left:0;top:0;width:58px;height:1022px;background:var(--sidebar)}
.menu-icon{position:absolute;left:15px;top:28px}
.nav-item{position:absolute;left:0;width:58px;height:36px;display:flex;align-items:center;justify-content:center}
.nav-item.active::before{content:"";position:absolute;left:0;top:0;width:3px;height:36px;background:var(--green)}
.page-title{position:absolute;left:92px;top:28px;font-size:23px;font-weight:700}
.topbar{position:absolute;right:36px;top:26px;display:flex;align-items:center;gap:14px}
.avatar{width:44px;height:44px;border-radius:50%;background:linear-gradient(#c9a68a,#e8742f)}
.user-name{font-size:13px;font-weight:700;line-height:1.1}
.user-role{font-size:10.5px;color:var(--muted)}
.tab{position:absolute;height:31px;display:flex;align-items:center;justify-content:center;gap:6px;font-size:10.5px;font-weight:600;border-radius:6px 6px 0 0}
.tab-search{left:93px;top:95px;width:130px;background:var(--green);color:#fff}
.tab-order{left:232px;top:95px;width:130px;background:#fff}
.form-panel{position:absolute;left:93px;top:126px;width:288px;height:920px;background:var(--panel);border-radius:0 18px 0 0;padding:32px 25px 0 25px}
.field{margin-bottom:7px}
.field label{display:block;font-size:10.5px;font-weight:600;margin-bottom:6px;letter-spacing:.2px}
.field .input{height:36px;background:var(--field);border-radius:3px;display:flex;align-items:center;justify-content:space-between;padding:0 16px;font-size:13.5px;color:var(--muted)}
.checkbox-row{display:flex;align-items:center;gap:8px;font-size:11.5px;font-weight:600;margin:20px 0 0 4px}
.checkbox{width:13px;height:13px;border-radius:2px;background:var(--red);display:flex;align-items:center;justify-content:center}
.actions{display:flex;gap:9px;margin:14px 0 0 4px}
.btn{width:114px;height:34px;border-radius:3px;display:flex;align-items:center;justify-content:center;gap:6px;font-size:12.5px;font-weight:600}
.btn-save{background:var(--green);color:#fff}
.btn-refresh{background:#e6e6e6;color:var(--text)}
.section-tabs{position:absolute;top:95px;left:397px;height:35px}
.section-tab{position:absolute;top:0;height:35px;display:flex;align-items:center;font-size:10.5px;font-weight:600}
.section-tab.active{background:var(--dark);color:#fff;border-radius:7px 7px 0 0;justify-content:center}
.table-panel{position:absolute;left:397px;top:130px;width:767px;height:920px;background:var(--panel);border-radius:14px 14px 0 0;padding:0 26px 0 18px}
table{border-collapse:collapse;width:723px;table-layout:fixed}
th{height:54px;font-size:11px;font-weight:500;text-align:left;border-bottom:2px solid var(--line)}
td{height:62px;font-size:12.5px;color:var(--muted);border-bottom:1px solid var(--line)}
td+td{border-left:1px solid var(--line)}
tr.group-end td{border-bottom:2px solid var(--line-strong)}
.c-type{width:104px;padding-left:30px}
.c-name{width:95px;padding-left:18px}
.c-att{width:185px;padding-left:31px}
.c-addr{width:199px;padding-left:39px}
.c-mail{width:140px;padding-left:28px}
</style>
</head>
<body>
<aside class="sidebar">
  <svg class="menu-icon" width="27" height="20" viewBox="0 0 27 20"><g stroke="#fff" stroke-width="2.4"><line x1="0" y1="2" x2="27" y2="2"/><line x1="0" y1="10" x2="27" y2="10"/><line x1="0" y1="18" x2="27" y2="18"/></g></svg>
  <div class="nav-item active" style="top:83px"><svg width="20" height="18" viewBox="0 0 20 18" fill="none" stroke="#2fd38a" stroke-width="1.5"><path d="M1 1h3l2 10h11l2-7H5"/><circle cx="8" cy="15" r="1.3"/><circle cx="15" cy="15" r="1.3"/></svg></div>
  <div class="nav-item" style="top:138px"><svg width="18" height="20" viewBox="0 0 18 20" fill="none" stroke="#fff" stroke-width="1.5"><rect x="2" y="2" width="14" height="17" rx="2"/><path d="M6 1v3M12 1v3M5 8h8M5 11h8M5 14h6"/></svg></div>
  <div class="nav-item" style="top:191px"><svg width="18" height="18" viewBox="0 0 18 18" fill="none" stroke="#fff" stroke-width="1.5"><circle cx="9" cy="9" r="7.5"/></svg></div>
  <div class="nav-item" style="top:246px"><svg width="20" height="22" viewBox="0 0 20 22" fill="none" stroke="#fff" stroke-width="1.5"><path d="M10 15s6-5 6-9a6 6 0 0 0-12 0c0 4 6 9 6 9z"/><circle cx="10" cy="6" r="2"/><path d="M5 14c-3 1-4 2-4 3 0 2 4 4 9 4s9-2 9-4c0-1-1-2-4-3"/></svg></div>
  <div class="nav-item" style="top:303px"><svg width="20" height="20" viewBox="0 0 20 20" fill="none" stroke="#fff" stroke-width="1.5"><circle cx="8" cy="6" r="4.5"/><path d="M1 19c0-4 3-6 7-6 2 0 3 .4 4 1M13 14h6M13 17h6"/></svg></div>
  <div class="nav-item" style="top:355px"><svg width="22" height="14" viewBox="0 0 22 14" fill="none" stroke="#fff" stroke-width="1.5"><path d="M1 7s4-6 10-6 10 6 10 6-4 6-10 6S1 7 1 7z"/><circle cx="11" cy="7" r="3"/></svg></div>
  <div class="nav-item" style="top:408px"><svg width="16" height="20" viewBox="0 0 16 20" fill="none" stroke="#fff" stroke-width="1.5"><rect x="1" y="8" width="14" height="11" rx="2"/><path d="M4 8V5a4 4 0 0 1 8 0v3M8 12v3"/></svg></div>
</aside>

<h1 class="page-title">Development</h1>

<div class="topbar">
  <svg width="22" height="22" viewBox="0 0 22 22" fill="none"><rect x="2" y="5" width="14" height="15" rx="2" stroke="#222631" stroke-width="1.8"/><circle cx="17" cy="4" r="3" fill="#fff" stroke="#ef5350" stroke-width="1.6"/></svg>
  <svg width="22" height="22" viewBox="0 0 22 22" fill="none" stroke="#222631" stroke-width="1.5"><circle cx="11" cy="11" r="9.5"/><path d="M8.5 8.5a2.5 2.5 0 1 1 3.5 2.3c-.7.3-1 .8-1 1.5V13"/><circle cx="11" cy="16" r=".6" fill="#222631"/></svg>
  <div class="avatar" role="img" aria-label="User profile photo"></div>
  <div><div class="user-name">JOHN DOE <svg width="9" height="6" viewBox="0 0 9 6" fill="none" stroke="#222631" stroke-width="1.4"><path d="M1 1l3.5 3.5L8 1"/></svg></div><div class="user-role">User role</div></div>
</div>

<div class="tab tab-search">ORDER SEARCH <svg width="10" height="10" viewBox="0 0 10 10"><circle cx="5" cy="5" r="5" fill="#fff"/><path d="M3.2 3.2l3.6 3.6M6.8 3.2L3.2 6.8" stroke="#2fd38a" stroke-width="1.3"/></svg></div>
<div class="tab tab-order">ORDER 9670363 <svg width="10" height="10" viewBox="0 0 10 10"><circle cx="5" cy="5" r="5" fill="#222631"/><path d="M3.2 3.2l3.6 3.6M6.8 3.2L3.2 6.8" stroke="#fff" stroke-width="1.3"/></svg></div>

<section class="form-panel">
  <div class="field"><label>ORDER NO*</label><div class="input">9670363</div></div>
  <div class="field"><label>BRAND*</label><div class="input">Verano</div></div>
  <div class="field"><label>ORDER TYPE*</label><div class="input">Sale</div></div>
  <div class="field"><label>STATUS*</label><div class="input">New</div></div>
  <div class="field"><label>ORIG ORDER NO*</label><div class="input">9670363</div></div>
  <div class="field"><label>REFERENCE*</label><div class="input">9670363</div></div>
  <div class="field"><label>ORDER CHANNEL*</label><div class="input">Standard</div></div>
  <div class="field"><label>LOCATION CODE*</label><div class="input">1301</div></div>
  <div class="field"><label>CUSTOMER NO*</label><div class="input">+08 123 456 <svg width="9" height="14" viewBox="0 0 9 14" fill="none" stroke="#222631" stroke-width="1.4"><path d="M1 5l3.5-3.5L8 5M1 9l3.5 3.5L8 9"/></svg></div></div>
  <div class="field"><label>FIRST NAME*</label><div class="input">John</div></div>
  <div class="field"><label>SURNAME*</label><div class="input">John doe</div></div>
  <div class="field"><label>EMAIL*</label><div class="input">Info@example.com</div></div>
  <div class="checkbox-row">AUTHORITY TO LEAVE <span class="checkbox"><svg width="9" height="7" viewBox="0 0 9 7" fill="none" stroke="#fff" stroke-width="1.6"><path d="M1 3.5l2.3 2.3L8 1"/></svg></span></div>
  <div class="actions">
    <div class="btn btn-save"><svg width="16" height="16" viewBox="0 0 16 16" fill="none" stroke="#fff" stroke-width="1.5"><path d="M1 1h11l3 3v11H1z"/><rect x="4" y="9" width="8" height="6"/><path d="M4 1v4h6V1"/></svg>SAVE</div>
    <div class="btn btn-refresh"><svg width="18" height="16" viewBox="0 0 18 16" fill="none" stroke="#222631" stroke-width="1.5"><path d="M15 6a7 7 0 0 0-13 1M3 10a7 7 0 0 0 13-1M15 2v4h-4M3 14v-4h4"/></svg>REFRESH</div>
  </div>
</section>

<nav class="section-tabs">
  <div class="section-tab" style="left:10px">ITEMS</div>
  <div class="section-tab" style="left:67px">CUSTOMER (S)</div>
  <div class="section-tab active" style="left:167px;width:95px">ADDRESSES</div>
  <div class="section-tab" style="left:278px">PAYMENTS</div>
  <div class="section-tab" style="left:360px">VOUCHERS</div>
  <div class="section-tab" style="left:443px">EVENT QUEUES</div>
  <div class="section-tab" style="left:543px">UPDATES</div>
  <div class="section-tab" style="left:616px">FULFILMENTS</div>
  <div class="section-tab" style="left:709px">HISTORY</div>
</nav>

<section class="table-panel">
  <table>
    <thead><tr><th class="c-type">TYPE</th><th class="c-name">NAME</th><th class="c-att">ATTENTION OF</th><th class="c-addr">ADDRESS</th><th class="c-mail">EMAIL</th></tr></thead>
    <tbody>
      <tr><td class="c-type">Delivery</td><td class="c-name">Test Order</td><td class="c-att"></td><td class="c-addr">Some address line here</td><td class="c-mail">info@example.com</td></tr>
      <tr><td class="c-type">Delivery</td><td class="c-name">Test Order</td><td class="c-att"></td><td class="c-addr">Some address line here</td><td class="c-mail">info@example.com</td></tr>
      <tr class="group-end"><td class="c-type">Delivery</td><td class="c-name">Test Order</td><td class="c-att"></td><td class="c-addr">Some address line here</td><td class="c-mail">info@example.com</td></tr>
      <tr><td class="c-type">Delivery</td><td class="c-name">Test Order</td><td class="c-att"></td><td class="c-addr">Some address line here</td><td class="c-mail">info@example.com</td></tr>
      <tr><td class="c-type">Delivery</td><td class="c-name">Test Order</td><td class="c-att"></td><td class="c-addr">Some address line here</td><td class="c-mail">info@example.com</td></tr>
      <tr class="group-end"><td class="c-type">Delivery</td><td class="c-name">Test Order</td><td class="c-att"></td><td class="c-addr">Some address line here</td><td class="c-mail">info@example.com</td></tr>
      <tr><td class="c-type">Delivery</td><td class="c-name">Test Order</td><td class="c-att"></td><td class="c-addr">Some address line here</td><td class="c-mail">info@example.com</td></tr>
      <tr><td class="c-type">Delivery</td><td class="c-name">Test Order</td><td class="c-att"></td><td class="c-addr">Some address line here</td><td class="c-mail">info@example.com</td></tr>
      <tr class="group-end"><td class="c-type">Delivery</td><td class="c-name">Test Order</td><td class="c-att"></td><td class="c-addr">Some address line here</td><td class="c-mail">info@example.com</td></tr>
      <tr><td class="c-type">Delivery</td><td class="c-name">Test Order</td><td class="c-att"></td><td class="c-addr">Some address line here</td><td class="c-mail">info@example.com</td></tr>
      <tr><td class="c-type">Delivery</td><td class="c-name">Test Order</td><td class="c-att"></td><td class="c-addr">Some address line here</td><td class="c-mail">info@example.com</td></tr>
      <tr class="group-end"><td class="c-type">Delivery</td><td class="c-name">Test Order</td><td class="c-att"></td><td class="c-addr">Some address line here</td><td class="c-mail">info@example.com</td></tr>
      <tr><td class="c-type">Delivery</td><td class="c-name">Test Order</td><td class="c-att"></td><td class="c-addr">Some address line here</td><td class="c-mail">info@example.com</td></tr>
    </tbody>
  </table>
</section>
</body>
</html>
```